Building company buisness cards

We are looking for a sharp modern new look for our business cards.
We are a New Zealand based company that specialises in house and land packages.
We have attached a photo of the current logo and would like to see if it can be improved somehow if needed.
We are open to any colours but we have chosen green at this stage.
Feel free to change the font and make the logo smarter looking.
Play with the colours and see what looks best.

We want a card that looks so good know one will want to throw it away!

Target Market(s)

Home buyers

Industry/Entity Type

Building

Contact Information for Business Card

Dorian Keswick
0217392604
dkeswick@tidewellhomecraft.co.nz
tidewellhomecraft.co.nz

Font styles to use
Serif
Sans Serif

Colors

Designer to choose colors to be used in the design.

Requirements
Must have
• Logo and company name on one side, details on the other side
Nice to have
• Color codes for the original green are HEX #4a8028, RGB(74,128,40), CMYK(42,0,69,50)
• Round corners, Raised and/or spot UV

```html
<!DOCTYPE html>
<html lang="en">
<head>
<meta charset="utf-8">
<title>Tidewell Homecraft – Business Cards</title>
<link rel="stylesheet" href="https://fonts.googleapis.com/css2?family=Arimo:wght@400;700&family=Nunito:wght@800&display=swap">
<style>
  :root {
    --backdrop: #ece6dc;
    --brand-green: #1f7010;
    --ink-dark: #2a2a2a;
    --paper: #fafafa;
    --text-grey: #2b2b2b;
    --white: #ffffff;
  }
  html, body {
    margin: 0;
    padding: 0;
    width: 1200px;
    height: 1199px;
    overflow: hidden;
    background: var(--backdrop);
  }
  .canvas {
    position: relative;
    width: 1200px;
    height: 1199px;
  }
  .card {
    position: absolute;
    width: 751px;
    height: 429px;
    box-shadow: 0 6px 14px rgba(0, 0, 0, 0.28);
  }
  .card svg { display: block; width: 100%; height: 100%; }
  .card--front { left: 173px; top: 173px; }
  .card--back  { left: 243px; top: 659px; }
  .fill-green { fill: var(--brand-green); }
  .fill-dark  { fill: var(--ink-dark); }
  .fill-paper { fill: var(--paper); }
  .brand-name {
    font-family: "Nunito", sans-serif;
    font-weight: 800;
    fill: var(--brand-green);
  }
  .brand-mark { fill: var(--brand-green); }
  .web-address {
    font-family: "Arimo", sans-serif;
    font-weight: 400;
    font-size: 27px;
    fill: var(--text-grey);
  }
  .contact {
    font-family: "Arimo", sans-serif;
    font-weight: 700;
    fill: var(--white);
  }
  .contact--name { font-size: 31px; }
  .contact--line { font-size: 22px; }
  .brand-ghost {
    font-family: "Nunito", sans-serif;
    font-weight: 800;
    font-size: 22px;
    fill: var(--white);
    opacity: 0.45;
  }
</style>
</head>
<body>
<main class="canvas">

  <section class="card card--front" aria-label="Card front">
    <svg viewBox="0 0 695 397" xmlns="http://www.w3.org/2000/svg">
      <defs>
        <filter id="panel-shadow" x="-10%" y="-10%" width="120%" height="120%">
          <feDropShadow dx="0" dy="0" stdDeviation="6" flood-color="#000" flood-opacity="0.45"/>
        </filter>
      </defs>
      <rect class="fill-dark" width="695" height="397"/>
      <polygon class="fill-green" points="0,0 125,0 68,190"/>
      <polygon class="fill-green" points="628,190 695,397 557,397" filter="url(#panel-shadow)"/>
      <polygon class="fill-paper" points="125,0 680,0 557,397 0,397" filter="url(#panel-shadow)"/>
      <circle class="brand-mark" cx="222" cy="115" r="16"/>
      <text class="brand-name" x="250" y="134" font-size="36">tidewell</text>
      <text class="brand-name" x="202" y="188" font-size="36">homecraft</text>
      <text class="web-address" x="104" y="337">tidewellhomecraft.co.nz</text>
    </svg>
  </section>

  <section class="card card--back" aria-label="Card back">
    <svg viewBox="0 0 695 397" xmlns="http://www.w3.org/2000/svg">
      <defs>
        <filter id="panel-shadow-back" x="-10%" y="-10%" width="120%" height="120%">
          <feDropShadow dx="0" dy="0" stdDeviation="6" flood-color="#000" flood-opacity="0.45"/>
        </filter>
      </defs>
      <rect class="fill-dark" width="695" height="397"/>
      <polygon class="fill-paper" points="570,0 695,0 636,192"/>
      <polygon class="fill-paper" points="70,190 140,397 0,397"/>
      <polygon class="fill-green" points="15,0 570,0 695,397 140,397" filter="url(#panel-shadow-back)"/>
      <text class="brand-ghost" x="498" y="68" text-anchor="middle">tidewell</text>
      <text class="brand-ghost" x="498" y="96" text-anchor="middle">homecraft</text>
      <text class="contact contact--name" x="129" y="213">Dorian Keswick</text>
      <text class="contact contact--line" x="148" y="263">0217392604</text>
      <text class="contact contact--line" x="162" y="304">dkeswick@tidewellhomecraft.co.nz</text>
      <text class="contact contact--line" x="175" y="344">tidewellhomecraft.co.nz</text>
    </svg>
  </section>

</main>
</body>
</html>
```